Drifting Earwaves - listen to podcasts from around the world

http://randompodcasts.com/Drifting Earwaves lets you listen to randomly selected podcasts from around the world. You can filter the podcasts by language. The power of randomness allows you to escape filter bubbles and echo chambers and discover issues and perspectives that you never knew existed. The current website offers basic functionality and is only a demo. Don't assume that anything in the current "design" should stay in place. The goal of the design should be to make it as easy as possible to understand what the app offers, to listen to new podcasts, and to skip to the next podcast. The service will be offered both as mobile apps and directly on the website. We expect that most users will be on mobile devices which is why we are focusing on the mobile/web app design.In addition to the current functionality, the app should also offer search (allowing the user to listen to podcasts that match given keywords), allow the user to easily subscribe to the current podcast and show the profile picture of the current podcast.

Target Market(s)

People interested in podcasts, all around the world

Colors

Designer to choose colors to be used in the design.

Requirements
Must have
• The main challenge is how to communicate the concept of the app to the user. Podcasts are randomly selected and the user just skips to the next one when he/she wants to. The ability to filter podcasts by language is important but no other filters are needed. The point is to use the power of random selection to explore new surprising content.
Nice to have
• The app/website is targeting a global audience. The less reliant the design is on written language, the better.

```html
<!DOCTYPE html>
<html lang="en">
<head>
<meta charset="utf-8">
<title>Drifting Earwaves – app screens</title>
<link href="https://fonts.googleapis.com/css2?family=Montserrat:wght@700;800&family=Roboto:wght@300;400;500&display=swap" rel="stylesheet">
<style>
:root{
  --stage-top:#2f3a50;
  --stage-bottom:#1c2333;
  --screen-top:#1d2436;
  --screen-bottom:#0e131e;
  --map-tone:#232b3f;
  --orange-red:#e5482a;
  --orange:#ef8a1c;
  --yellow:#f4c511;
  --text:#ffffff;
  --text-soft:#c9ccd4;
  --rule:#3a4256;
  --menu-rule:rgba(255,255,255,.35);
}
*{box-sizing:border-box;margin:0;padding:0}
html,body{width:1200px;height:954px;overflow:hidden}
body{
  background:radial-gradient(ellipse at 50% 40%,var(--stage-top),var(--stage-bottom));
  font-family:"Roboto",Arial,sans-serif;font-weight:300;color:var(--text);
  position:relative;
}
.screen{
  position:absolute;overflow:hidden;
  background:linear-gradient(180deg,var(--screen-top),var(--screen-bottom));
  box-shadow:0 14px 30px rgba(0,0,0,.45);
}
.screen--hero{left:34px;top:83px;width:404px;height:717px}
.screen--small{width:226px;height:402px}
.col-1{left:461px}.col-2{left:703px}.col-3{left:945px}
.row-1{top:83px}.row-2{top:501px}
.wave{position:absolute;left:0;top:0;width:100%}
.map-area{position:absolute;left:0;width:100%;background:radial-gradient(ellipse at 50% 50%,var(--map-tone),transparent 70%)}
.burger{position:absolute;width:16px;height:11px;
  background:linear-gradient(var(--text) 0 2px,transparent 2px 4.5px,var(--text) 4.5px 6.5px,transparent 6.5px 9px,var(--text) 9px 11px)}
.screen--hero .burger{left:47px;top:124px;width:27px;height:20px;
  background:linear-gradient(var(--text) 0 3px,transparent 3px 8.5px,var(--text) 8.5px 11.5px,transparent 11.5px 17px,var(--text) 17px 20px)}
.screen--small .burger{left:23px;top:87px}
.center{position:absolute;left:0;width:100%;text-align:center}
.rule{position:absolute;height:1px;background:var(--rule)}
.btn{position:absolute;display:flex;align-items:center;justify-content:center;
  background:linear-gradient(90deg,var(--orange-red),var(--orange) 55%,var(--yellow));
  color:var(--text);font-weight:300}
.hero-mark{position:absolute;left:172px;top:245px;width:60px;height:60px;border-radius:50%;border:5px solid var(--text)}
.hero-title{top:361px;font-family:"Montserrat",Arial,sans-serif;font-weight:800;font-size:30px;line-height:29px;letter-spacing:.5px}
.hero-copy{top:449px;font-size:19.5px;line-height:23px;color:var(--text-soft)}
.heading{font-family:"Montserrat",Arial,sans-serif;font-weight:700;font-size:17px}
.label{font-size:11px;color:var(--text-soft)}
.tiny{font-size:6.5px;color:var(--text-soft);letter-spacing:.2px}
.cover{position:absolute;border:2px solid #e8dcb0}
.cover--main{background:linear-gradient(135deg,#3b3a2a,#c8a243 45%,#2d2a22)}
.cover--side-a{background:linear-gradient(135deg,#f1c6a0,#d3462f)}
.cover--side-b{background:linear-gradient(135deg,#37c3c9,#e8b62c)}
.episode{font-size:10px;line-height:10px;color:var(--text-soft)}
.episode b{font-weight:400;color:var(--text)}
.meta{font-size:10px;line-height:13px;color:var(--text-soft)}
.meta b{font-weight:400;color:var(--text)}
.progress{position:absolute;left:31px;width:163px;height:2px;background:#d9dbe0}
.progress i{position:absolute;top:-2px;width:5px;height:5px;border-radius:50%;background:#fff}
.time{position:absolute;font-size:4px;color:#8d93a3}
.controls{position:absolute;left:31px;width:163px;height:14px}
.screen--menu{background:linear-gradient(90deg,var(--orange-red),var(--orange))}
.menu-title{top:32px;font-family:"Montserrat",Arial,sans-serif;font-weight:700;font-size:17px}
.menu-title span{margin-left:12px}
.menu-item{font-size:10.5px;color:#ffe7d6}
.menu-lang{font-size:8px;color:rgba(255,255,255,.45)}
.menu-lang--on{color:var(--text);font-weight:400}
.menu-rule{position:absolute;left:59px;width:114px;height:1px;background:var(--menu-rule)}
.search{position:absolute;left:60px;top:348px;width:113px;height:28px;background:rgba(255,255,255,.35)}
</style>
</head>
<body>

<!-- Welcome screen -->
<section class="screen screen--hero">
  <svg class="wave" height="240" viewBox="0 0 404 240" preserveAspectRatio="none" aria-hidden="true">
    <defs><linearGradient id="g1" x1="0" x2="1"><stop offset="0" stop-color="#e5482a"/><stop offset=".5" stop-color="#ef8a1c"/><stop offset="1" stop-color="#f4c511"/></linearGradient></defs>
    <path d="M0 0H404V225C320 235 240 120 150 110C90 100 40 115 0 100Z" fill="#2a2330"/>
    <path d="M0 0H404V208C320 215 240 100 150 92C90 85 40 95 0 82Z" fill="#4a3320"/>
    <path d="M0 0H404V192C320 198 240 85 150 76C90 70 40 78 0 64Z" fill="#6a4618"/>
    <path d="M0 0H404V172C320 178 240 66 150 58C90 52 40 58 0 44Z" fill="url(#g1)"/>
  </svg>
  <div class="burger"></div>
  <div class="map-area" style="top:200px;height:240px" role="img" aria-label="Faint world map with glowing location dots"></div>
  <div class="hero-mark"></div>
  <div class="center hero-title">DRIFTING<br>EARWAVES</div>
  <div class="rule" style="left:104px;width:204px;top:429px"></div>
  <div class="center hero-copy">Travel outside of your<br>echo chamber and filter<br>bubble, listen to podcasts<br>from around the world</div>
  <div class="rule" style="left:106px;width:204px;top:558px"></div>
  <div class="btn" style="left:105px;top:579px;width:204px;height:42px;font-size:19px">ENTER</div>
</section>

<!-- Sign up -->
<section class="screen screen--small col-1 row-1">
  <svg class="wave" height="100" viewBox="0 0 226 100" preserveAspectRatio="none" aria-hidden="true">
    <path d="M0 0H226V98C180 100 140 50 90 42C55 37 25 44 0 36Z" fill="#3a2a25"/>
    <path d="M0 0H226V88C180 90 140 40 90 33C55 28 25 33 0 26Z" fill="#6a4618"/>
    <path d="M0 0H226V78C180 80 140 30 90 24C55 19 25 24 0 16Z" fill="url(#g1)"/>
  </svg>
  <div class="burger"></div>
  <div class="map-area" style="top:100px;height:130px" role="img" aria-label="Faint world map with location dots"></div>
  <div class="center heading" style="top:248px">SIGN UP</div>
  <div class="rule" style="left:58px;width:115px;top:278px"></div>
  <div class="center label" style="top:290px">No thanks</div>
  <div class="rule" style="left:58px;width:115px;top:314px"></div>
</section>

<!-- Log in -->
<section class="screen screen--small col-2 row-1">
  <svg class="wave" height="100" viewBox="0 0 226 100" preserveAspectRatio="none" aria-hidden="true">
    <path d="M0 0H226V98C180 100 140 50 90 42C55 37 25 44 0 36Z" fill="#3a2a25"/>
    <path d="M0 0H226V88C180 90 140 40 90 33C55 28 25 33 0 26Z" fill="#6a4618"/>
    <path d="M0 0H226V78C180 80 140 30 90 24C55 19 25 24 0 16Z" fill="url(#g1)"/>
  </svg>
  <div class="burger"></div>
  <div class="map-area" style="top:100px;height:130px" role="img" aria-label="Faint world map with location dots"></div>
  <div class="center label" style="top:254px">EMAIL ADRESS</div>
  <div class="rule" style="left:58px;width:115px;top:278px"></div>
  <div class="center label" style="top:290px">PASSWORD</div>
  <div class="rule" style="left:58px;width:115px;top:314px"></div>
  <div class="btn" style="left:58px;top:325px;width:115px;height:22px;font-size:10px">ENTER</div>
  <div class="center tiny" style="top:364px">FORGOT YOUR PASSWORD?</div>
</section>

<!-- Player: browse -->
<section class="screen screen--small col-3 row-1">
  <svg class="wave" height="100" viewBox="0 0 226 100" preserveAspectRatio="none" aria-hidden="true">
    <path d="M0 0H226V98C180 100 140 50 90 42C55 37 25 44 0 36Z" fill="#3a2a25"/>
    <path d="M0 0H226V88C180 90 140 40 90 33C55 28 25 33 0 26Z" fill="#6a4618"/>
    <path d="M0 0H226V78C180 80 140 30 90 24C55 19 25 24 0 16Z" fill="url(#g1)"/>
  </svg>
  <div class="burger"></div>
  <div class="map-area" style="top:100px;height:150px" role="img" aria-label="Faint world map"></div>
  <div style="position:absolute;left:28px;top:121px;width:6px;height:6px;border-radius:50%;background:var(--yellow);box-shadow:0 0 6px var(--orange)"></div>
  <div class="center label" style="top:117px;left:12px;font-size:10px">português / Portuguese (344)</div>
  <div class="center label" style="top:143px;font-size:10px">all</div>
  <div class="rule" style="left:62px;width:115px;top:162px"></div>
  <div class="cover cover--side-a" style="left:25px;top:198px;width:46px;height:62px" role="img" aria-label="Podcast cover art"></div>
  <div class="cover cover--side-b" style="left:153px;top:198px;width:46px;height:62px" role="img" aria-label="Podcast cover art"></div>
  <div class="cover cover--main" style="left:64px;top:179px;width:89px;height:89px" role="img" aria-label="Current podcast cover art"></div>
  <div class="center episode" style="top:290px">Episode &nbsp;#212 - Cidades inquietas<br>(feat. Lia Moraes e Rita)</div>
  <div class="rule" style="left:62px;width:115px;top:323px"></div>
  <div class="progress" style="top:341px"><i style="left:41px"></i></div>
  <div class="time" style="left:31px;top:345px">1:27</div>
  <div class="time" style="left:186px;top:345px">2:45</div>
  <svg class="controls" style="top:357px" viewBox="0 0 163 14" aria-label="Player controls">
    <g fill="none" stroke="#fff" stroke-width="1.3"><path d="M3 5h10l-2-2M13 9H3l2 2"/><path d="M148 4h4l6 6h3M148 10h4l6-6h3"/></g>
    <g fill="#fff"><rect x="36" y="3" width="1.5" height="8"/><path d="M45 3v8l-7-4zM52 3v8l-7-4z"/>
    <path d="M76 3v8l7-4z"/><rect x="88" y="3" width="1.3" height="8"/><rect x="91" y="3" width="1.3" height="8"/>
    <path d="M111 3v8l7-4zM118 3v8l7-4z"/><rect x="125" y="3" width="1.5" height="8"/></g>
  </svg>
</section>

<!-- Player: now playing -->
<section class="screen screen--small col-1 row-2">
  <svg class="wave" height="100" viewBox="0 0 226 100" preserveAspectRatio="none" aria-hidden="true">
    <path d="M0 0H226V98C180 100 140 50 90 42C55 37 25 44 0 36Z" fill="#3a2a25"/>
    <path d="M0 0H226V88C180 90 140 40 90 33C55 28 25 33 0 26Z" fill="#6a4618"/>
    <path d="M0 0H226V78C180 80 140 30 90 24C55 19 25 24 0 16Z" fill="url(#g1)"/>
  </svg>
  <div class="burger"></div>
  <div class="cover cover--main" style="left:70px;top:101px;width:88px;height:88px" role="img" aria-label="Current podcast cover art"></div>
  <div class="center episode" style="top:213px"><b>Episode</b> #212 - Cidades inquietas<br>(feat. Lia Moraes e Rita)</div>
  <div class="rule" style="left:56px;width:115px;top:251px"></div>
  <div class="center label" style="top:258px;font-size:10px">more Info</div>
  <div class="rule" style="left:56px;width:115px;top:277px"></div>
  <svg style="position:absolute;left:32px;top:287px" width="162" height="48" viewBox="0 0 162 48" aria-label="Audio waveform">
    <defs><linearGradient id="wf" x1="0" y1="1" x2="0" y2="0"><stop offset="0" stop-color="#8a1e14"/><stop offset="1" stop-color="#f0851c"/></linearGradient></defs>
    <g fill="url(#wf)">
      <rect x="0" y="30" width="1.6" height="18"/><rect x="3.5" y="22" width="1.6" height="26"/><rect x="7" y="34" width="1.6" height="14"/><rect x="10.5" y="18" width="1.6" height="30"/><rect x="14" y="28" width="1.6" height="20"/><rect x="17.5" y="14" width="1.6" height="34"/><rect x="21" y="32" width="1.6" height="16"/><rect x="24.5" y="24" width="1.6" height="24"/><rect x="28" y="36" width="1.6" height="12"/><rect x="31.5" y="20" width="1.6" height="28"/><rect x="35" y="30" width="1.6" height="18"/><rect x="38.5" y="16" width="1.6" height="32"/><rect x="42" y="26" width="1.6" height="22"/><rect x="45.5" y="34" width="1.6" height="14"/><rect x="49" y="22" width="1.6" height="26"/><rect x="52.5" y="30" width="1.6" height="18"/><rect x="56" y="18" width="1.6" height="30"/><rect x="59.5" y="32" width="1.6" height="16"/><rect x="63" y="24" width="1.6" height="24"/><rect x="66.5" y="12" width="1.6" height="36"/><rect x="70" y="28" width="1.6" height="20"/><rect x="73.5" y="20" width="1.6" height="28"/><rect x="77" y="34" width="1.6" height="14"/><rect x="80.5" y="22" width="1.6" height="26"/><rect x="84" y="30" width="1.6" height="18"/><rect x="87.5" y="16" width="1.6" height="32"/><rect x="91" y="26" width="1.6" height="22"/><rect x="94.5" y="20" width="1.6" height="28"/><rect x="98" y="32" width="1.6" height="16"/><rect x="101.5" y="24" width="1.6" height="24"/><rect x="105" y="30" width="1.6" height="18"/><rect x="108.5" y="14" width="1.6" height="34"/><rect x="112" y="26" width="1.6" height="22"/><rect x="115.5" y="34" width="1.6" height="14"/><rect x="119" y="18" width="1.6" height="30"/><rect x="122.5" y="2" width="1.6" height="46"/><rect x="126" y="16" width="1.6" height="32"/><rect x="129.5" y="28" width="1.6" height="20"/><rect x="133" y="22" width="1.6" height="26"/><rect x="136.5" y="32" width="1.6" height="16"/><rect x="140" y="20" width="1.6" height="28"/><rect x="143.5" y="28" width="1.6" height="20"/><rect x="147" y="14" width="1.6" height="34"/><rect x="150.5" y="30" width="1.6" height="18"/><rect x="154" y="22" width="1.6" height="26"/><rect x="157.5" y="26" width="1.6" height="22"/>
    </g>
  </svg>
  <div class="progress" style="top:341px"><i style="left:50px"></i></div>
  <div class="time" style="left:31px;top:345px">1:27</div>
  <div class="time" style="left:186px;top:345px">2:45</div>
  <svg class="controls" style="top:357px" viewBox="0 0 163 14" aria-label="Player controls">
    <g fill="none" stroke="#fff" stroke-width="1.3"><path d="M3 5h10l-2-2M13 9H3l2 2"/><path d="M148 4h4l6 6h3M148 10h4l6-6h3"/></g>
    <g fill="#fff"><rect x="36" y="3" width="1.5" height="8"/><path d="M45 3v8l-7-4zM52 3v8l-7-4z"/>
    <path d="M76 3v8l7-4z"/><rect x="88" y="3" width="1.3" height="8"/><rect x="91" y="3" width="1.3" height="8"/>
    <path d="M111 3v8l7-4zM118 3v8l7-4z"/><rect x="125" y="3" width="1.5" height="8"/></g>
  </svg>
</section>

<!-- Episode info -->
<section class="screen screen--small col-2 row-2">
  <svg class="wave" height="100" viewBox="0 0 226 100" preserveAspectRatio="none" aria-hidden="true">
    <path d="M0 0H226V98C180 100 140 50 90 42C55 37 25 44 0 36Z" fill="#3a2a25"/>
    <path d="M0 0H226V88C180 90 140 40 90 33C55 28 25 33 0 26Z" fill="#6a4618"/>
    <path d="M0 0H226V78C180 80 140 30 90 24C55 19 25 24 0 16Z" fill="url(#g1)"/>
  </svg>
  <div class="burger"></div>
  <div class="cover cover--main" style="left:70px;top:43px;width:89px;height:89px" role="img" aria-label="Current podcast cover art"></div>
  <div class="center episode" style="top:151px"><b>Episode</b> #212 - Cidades inquietas<br>(feat. Lia Moraes e Rita)</div>
  <div class="center meta" style="top:192px"><b>Published</b> 8 days ago</div>
  <div class="center meta" style="top:220px"><b>Language</b> português / Portuguese</div>
  <div class="meta" style="position:absolute;left:31px;top:254px"><b>Location</b></div>
  <div class="meta" style="position:absolute;right:33px;top:254px;text-align:right">United States (ip-country)<br>Germany (domain-country)<br>Brazil (charts-top-country)</div>
  <div class="btn" style="left:58px;top:324px;width:115px;height:23px;font-size:10px">BACK</div>
  <svg style="position:absolute;left:58px;top:364px" width="116" height="14" viewBox="0 0 116 14" aria-label="Download, react, favourite">
    <g fill="none" stroke="#ef8a1c" stroke-width="1.4"><path d="M8 1v8M5 6l3 3 3-3M2 10v3h12v-3"/><circle cx="57" cy="7" r="5.8"/><path d="M54 8.5c1.6 2 4.4 2 6 0"/></g>
    <g fill="#ef8a1c"><circle cx="55" cy="5.5" r=".9"/><circle cx="59" cy="5.5" r=".9"/><path d="M108 0.5l1.9 4.2 4.6.4-3.5 3 1.1 4.5-4.1-2.4-4.1 2.4 1.1-4.5-3.5-3 4.6-.4z"/></g>
  </svg>
</section>

<!-- Menu -->
<section class="screen screen--small col-3 row-2 screen--menu">
  <div class="center menu-title">✕<span>MENU</span></div>
  <div class="menu-rule" style="top:58px"></div>
  <div class="center menu-item" style="top:69px">Choose Language</div>
  <div class="center menu-lang" style="top:101px">Deutsch / German (1085)</div>
  <div class="center menu-lang menu-lang--on" style="top:118px">português / Portuguese (344)</div>
  <div class="center menu-lang" style="top:137px">español / Spanish (814)</div>
  <div class="menu-rule" style="top:177px"></div>
  <div class="center menu-item" style="top:185px">Music</div>
  <div class="menu-rule" style="top:208px"></div>
  <div class="center menu-item" style="top:217px">FM Radio</div>
  <div class="menu-rule" style="top:240px"></div>
  <div class="center menu-item" style="top:250px">Reportings</div>
  <div class="menu-rule" style="top:271px"></div>
  <div class="center menu-item" style="top:281px">all</div>
  <div class="menu-rule" style="top:303px"></div>
  <div class="center menu-item" style="top:313px">my List</div>
  <div class="menu-rule" style="top:335px"></div>
  <div class="search">
    <svg style="position:absolute;left:7px;top:7px" width="14" height="14" viewBox="0 0 14 14" aria-label="Search"><circle cx="5.5" cy="5.5" r="4" fill="none" stroke="#fff" stroke-width="1.8"/><path d="M8.5 8.5l4 4" stroke="#fff" stroke-width="2"/></svg>
  </div>
</section>

</body>
</html>
```